Baby Store - GIF Banner

About the Company:
Nalifa.com.sa is an online shop for baby related products in Saudi Arabia. The targeted audience is moms between 25-35 years of age. The word "Nalifa" means Shop/Store in the Arabic Language.
About the Banner:
The banners should be designed in animated GIF format and provide in four sizes, upon clicking on the banner it will take you to Nalifa website. The Banners will convey the following:
- All your baby daily needs
مستلزمات طفلك اليومية من نليفا
- Free same day delivery
توصيل مجاني بنفس اليوم في الرياض
- Subscribe now for special discounts.
سجلي الان لتحصلي على خصم خاص
Note: Arabic Text are attached in PSD format.
Design Requirements:
Company Logo is attached.
Sample of product photos will be provided.
Baby photo can be used.
Shop Now Button should be included in the design.
تسوق الان
Shop Now
Logo colors are the main colors to be used (Blue, Pink, Gray)
DropBox Link: will be provided upon request.
Design Style:
- Play full
- Feminine
- Creative
Delivery Requirements:
Initially we may start working on an English version, at the end you will must to provide an Arabic version of the Banners in addition to the English version. Arabic translations are provided above, Note that Arabic language is from right to left opposite to the English language.
Banners Sizes Required:
Banner 1: 728 x 90
Banner 2: 480 x 70
Banner 3: 300 x 250
Banner 4: 648x40
Banner Specs:
Size less than 100 kb
Background less than 80% alpha
Please pay EXTRA attention to the guidelines in the following link:
https://help.brivantomedia.net/clips/answer/530418
If you have any questions please let me know, wish you the best of luck.
Modern Moms of age 25-35.
Shop

```html
<!DOCTYPE html>
<html lang="en">
<head>
<meta charset="utf-8">
<title>Nalifa.com.sa – Baby Store Banner</title>
<link rel="stylesheet" href="https://fonts.googleapis.com/css2?family=Arvo:wght@400;700&family=Open+Sans:wght@700;800&display=swap">
<style>
  :root {
    --brand-blue: #2f74c8;
    --text-blue: #1f4fa6;
    --pink: #e24a8c;
    --pink-soft: #f7c9dc;
    --pink-pale: #fbe6ee;
    --blue-pale: #e3eefa;
    --gray: #8a8a8a;
    --white: #ffffff;
    --button-deep: #0b5fae;
    --button-light: #3ea6ea;
  }
  * { margin: 0; padding: 0; box-sizing: border-box; }
  html, body { width: 1200px; height: 138px; overflow: hidden; background: var(--white); }
  .banner {
    position: relative;
    width: 1200px;
    height: 138px;
    overflow: hidden;
    background: var(--white);
    font-family: "Arvo", serif;
  }
  .backdrop { position: absolute; inset: 0; }
  .brand {
    position: absolute;
    left: 66px;
    top: 40px;
    display: flex;
    align-items: center;
    gap: 10px;
  }
  .brand-dot {
    width: 18px; height: 18px; border-radius: 50%;
    background: var(--pink);
  }
  .brand-name {
    font-family: "Arvo", serif;
    font-weight: 700;
    font-size: 36px;
    color: var(--brand-blue);
    letter-spacing: -0.5px;
  }
  .baby-photo {
    position: absolute;
    left: 290px;
    top: 0;
    width: 300px;
    height: 138px;
    background: radial-gradient(ellipse at 45% 55%, #f3a9c6 0%, #f7c6da 45%, rgba(251,230,238,0.6) 75%, rgba(255,255,255,0) 100%);
  }
  .benefits {
    position: absolute;
    left: 534px;
    top: 10px;
    list-style: none;
  }
  .benefit {
    display: flex;
    align-items: center;
    height: 41px;
    gap: 16px;
  }
  .benefit-arrow { width: 30px; height: 26px; flex: none; }
  .benefit-text {
    font-weight: 700;
    font-size: 25px;
    color: var(--text-blue);
    white-space: nowrap;
  }
  .shop-now {
    position: absolute;
    left: 1072px;
    top: 16px;
    width: 92px;
    height: 92px;
    border-radius: 50%;
    background: radial-gradient(circle at 40% 30%, var(--button-light), var(--button-deep) 75%);
    border: 3px solid var(--white);
    box-shadow: 0 2px 6px rgba(0,0,0,0.3);
    display: flex;
    flex-direction: column;
    align-items: center;
    justify-content: center;
    font-family: "Open Sans", sans-serif;
    font-weight: 800;
    color: var(--white);
    font-size: 17px;
    line-height: 1.05;
    text-decoration: none;
  }
  .cart-icon {
    position: absolute;
    left: 1140px;
    top: 96px;
    width: 36px;
    height: 30px;
  }
</style>
</head>
<body>
<div class="banner">
  <svg class="backdrop" width="1200" height="138" viewBox="0 0 1200 138" aria-hidden="true">
    <circle cx="-20" cy="30" r="60" fill="var(--pink-soft)"/>
    <circle cx="10" cy="150" r="55" fill="var(--blue-pale)"/>
    <circle cx="40" cy="90" r="26" fill="var(--pink-pale)"/>
    <circle cx="960" cy="-10" r="70" fill="var(--blue-pale)"/>
    <circle cx="1010" cy="150" r="60" fill="var(--pink-pale)"/>
    <circle cx="1190" cy="20" r="55" fill="var(--pink-pale)"/>
    <circle cx="840" cy="130" r="32" fill="var(--blue-pale)"/>
  </svg>

  <div class="brand">
    <span class="brand-name">Nalifa.com.sa</span>
    <span class="brand-dot"></span>
  </div>

  <div class="baby-photo" role="img" aria-label="Photo of a smiling baby lying down, in soft pink tones"></div>

  <ul class="benefits">
    <li class="benefit">
      <svg class="benefit-arrow" viewBox="0 0 30 26" aria-hidden="true"><path d="M3 22 C6 12 12 8 20 8 L20 2 L29 11 L20 20 L20 14 C13 14 8 16 3 22 Z" fill="var(--pink)"/></svg>
      <span class="benefit-text">All your baby daily needs</span>
    </li>
    <li class="benefit">
      <svg class="benefit-arrow" viewBox="0 0 30 26" aria-hidden="true"><path d="M3 22 C6 12 12 8 20 8 L20 2 L29 11 L20 20 L20 14 C13 14 8 16 3 22 Z" fill="var(--pink)"/></svg>
      <span class="benefit-text">Free same day delivery</span>
    </li>
    <li class="benefit">
      <svg class="benefit-arrow" viewBox="0 0 30 26" aria-hidden="true"><path d="M3 22 C6 12 12 8 20 8 L20 2 L29 11 L20 20 L20 14 C13 14 8 16 3 22 Z" fill="var(--pink)"/></svg>
      <span class="benefit-text">Subscribe now for special discounts.</span>
    </li>
  </ul>

  <a class="shop-now" href="#"><span>SHOP</span><span>NOW</span></a>
  <svg class="cart-icon" viewBox="0 0 36 30" aria-hidden="true">
    <path d="M2 4 H8 L12 20 H30 L34 8 H10" fill="none" stroke="var(--gray)" stroke-width="2.5" stroke-linejoin="round" stroke-linecap="round"/>
    <circle cx="14" cy="26" r="2.5" fill="var(--gray)"/>
    <circle cx="28" cy="26" r="2.5" fill="var(--gray)"/>
  </svg>
</div>
</body>
</html>
```